Lebel for 500g Honey Jar

We want a design for a 500g honey bottle or Jar as shown in the attached image . All Requirement has been put in the attached brief document .
Also Logo and images have been uploaded . Feel free to play arround with the selected solor schemes .

Target Market(s)

Retail Market

Industry/Entity Type

FMCG

Colors
00AB8E
00BBA5
67D7C9
C6EFE9
E9F9F6
59FF00
82FF00
B8FF75
E3FFCB
F4FFEA
FFC000
F8CF3A
FAE287
FDF2CF
FEFAEE
F0912C
F2A743
F7CA91
FBE8D2
FDF5EE
EE7325
F08F49
F5BC92
FAE3D3
FDF4ED

Requirements
Must have
• The desing must contain the company Address, Logo , and Nutritional Facts
Nice to have
• Image of a honey Bee , see samples attahed

```html
<!DOCTYPE html>
<html lang="en">
<head>
<meta charset="UTF-8">
<title>Meadowly Pure Natural Honey – 500g Jar Label</title>
<link rel="stylesheet" href="https://fonts.googleapis.com/css2?family=Fredoka:wght@600&family=Poppins:wght@400;500;600&display=swap">
<style>
  :root {
    --label-cream: #FEF7DC;
    --honey-yellow: #FFC000;
    --honey-light: #F8CF3A;
    --ink: #1B1B1B;
    --brand-green: #00AB8E;
  }
  html, body {
    margin: 0;
    padding: 0;
    overflow: hidden;
  }
  .label {
    position: relative;
    width: 672px;
    height: 1200px;
    background: var(--label-cream);
    font-family: "Poppins", sans-serif;
    color: var(--ink);
    overflow: hidden;
  }
  .brand-name {
    position: absolute;
    top: 40px;
    left: 0;
    width: 100%;
    text-align: center;
    font-weight: 600;
    font-size: 50px;
    letter-spacing: 0.5px;
    color: var(--brand-green);
    margin: 0;
  }
  .tagline {
    position: absolute;
    top: 160px;
    left: 0;
    width: 100%;
    text-align: center;
    font-size: 48px;
    font-weight: 400;
    margin: 0;
  }
  .product-title {
    position: absolute;
    top: 228px;
    left: 0;
    width: 100%;
    text-align: center;
    margin: 0;
    font-family: "Fredoka", sans-serif;
    font-weight: 600;
    font-size: 150px;
    line-height: 1;
    letter-spacing: 2px;
    color: var(--honey-yellow);
    -webkit-text-stroke: 5px var(--ink);
    paint-order: stroke fill;
  }
  .bee-illustration {
    position: absolute;
    top: 450px;
    left: 176px;
    width: 320px;
    height: 430px;
    border-radius: 48%;
    background: radial-gradient(ellipse at 50% 62%, var(--honey-light) 0%, rgba(248, 207, 58, 0.35) 45%, rgba(254, 247, 220, 0) 72%);
  }
  .free-from {
    position: absolute;
    top: 890px;
    left: 88px;
    display: flex;
    align-items: center;
    gap: 18px;
  }
  .free-from__word {
    font-size: 128px;
    font-weight: 500;
    line-height: 1;
    color: var(--honey-yellow);
    margin: 0;
  }
  .free-from__list {
    list-style: none;
    margin: 10px 0 0;
    padding: 0;
    font-size: 27px;
    line-height: 1.2;
  }
  .packer {
    position: absolute;
    top: 1038px;
    left: 0;
    width: 100%;
    text-align: center;
    font-size: 27px;
    font-weight: 500;
    line-height: 1.35;
    margin: 0;
  }
  .net-weight {
    position: absolute;
    top: 1130px;
    left: 0;
    width: 100%;
    text-align: center;
    font-size: 31px;
    font-weight: 500;
    margin: 0;
  }
</style>
</head>
<body>
  <main class="label">
    <p class="brand-name">meadowly</p>
    <p class="tagline">100% pure natural</p>
    <h1 class="product-title">HONEY</h1>
    <div class="bee-illustration" role="img" aria-label="Line illustration of a honey bee with looping wings and a yellow striped body"></div>
    <div class="free-from">
      <p class="free-from__word">zero</p>
      <ul class="free-from__list">
        <li>additive</li>
        <li>colouring</li>
        <li>preservative</li>
      </ul>
    </div>
    <p class="packer">Packed &amp; Distributed by<br>Meadowfield Farms Limited</p>
    <p class="net-weight">Net WT: 500g</p>
  </main>
</body>
</html>
```